Business card with logo for a family psychologist

I need a business card for my private practice in the urban Chicago area as a psychologist. I see families and individuals who are going through difficult times - divorce, separation, illness, or trauma. I want to project hopefulness, competence, and caring.

Target Market(s)

Adults, other professionals - such as physicans and lawyers

Industry/Entity Type

Health Care

Contact Information for Business Card

Front should have my name and credentials; back should have location information including my email, phone

Font styles to use
Serif
Decorative
Script

Requirements
Must have
• Unique logo
Should not have
• No pictures or icons of people; no black

```html
<!DOCTYPE html>
<html lang="en">
<head>
<meta charset="utf-8">
<title>Business Card – Psychologist</title>
<link href="https://fonts.googleapis.com/css2?family=Roboto:wght@300;400;500&display=swap" rel="stylesheet">
<style>
  :root {
    --teal: #16a9cc;
    --teal-deep: #0b8fb3;
    --text-grey: #8a8f94;
    --faint: #eef2f4;
    --card: #ffffff;
    --card-shade: #eceeef;
    --bg: #e4e6e8;
  }
  html, body {
    margin: 0;
    width: 1200px;
    height: 1023px;
    overflow: hidden;
    background: var(--bg);
    font-family: "Roboto", Arial, sans-serif;
  }
  .sheet {
    position: relative;
    width: 1200px;
    height: 1023px;
  }
  .card {
    position: absolute;
    left: 250px;
    width: 700px;
    height: 400px;
    border-radius: 22px;
    background: linear-gradient(160deg, var(--card) 0%, var(--card) 55%, var(--card-shade) 100%);
    box-shadow: 0 6px 18px rgba(0,0,0,.15);
    overflow: hidden;
  }
  .card--front { top: 60px; }
  .card--back { top: 540px; }

  /* front */
  .front__tab {
    position: absolute; left: 0; top: 0;
    width: 58px; height: 30px;
    background: var(--teal);
  }
  .front__person { position: absolute; left: 74px; top: 22px; }
  .front__name {
    margin: 0; color: var(--teal-deep);
    font-size: 30px; font-weight: 500; letter-spacing: 1px;
  }
  .front__title {
    margin: 4px 0 0; color: var(--text-grey);
    font-size: 16px; font-weight: 300; letter-spacing: 1.5px;
  }
  .brand {
    position: absolute; display: flex; align-items: center; gap: 22px;
  }
  .brand__dot { border: 6px solid var(--teal); border-radius: 50%; box-sizing: border-box; }
  .brand__name { color: var(--teal); font-weight: 500; letter-spacing: 1px; margin: 0; }
  .front__brand { left: 150px; top: 190px; }
  .front__brand .brand__dot { width: 120px; height: 120px; }
  .front__brand .brand__name { font-size: 44px; }

  /* back */
  .back__band { position: absolute; left: 0; top: 0; width: 120px; height: 400px; }
  .back__decor {
    position: absolute; right: -40px; top: -60px;
    width: 340px; height: 340px; border-radius: 50%;
    border: 18px solid var(--faint); box-sizing: border-box;
  }
  .back__brand { left: 110px; top: 60px; }
  .back__brand .brand__dot { width: 70px; height: 70px; border-width: 4px; }
  .back__brand .brand__name { font-size: 30px; }
  .back__divider {
    position: absolute; left: 110px; right: 40px; top: 170px;
    height: 1px; background: #c9d3e6;
  }
  .contact { position: absolute; left: 140px; top: 200px; margin: 0; padding: 0; list-style: none; }
  .contact__item {
    display: flex; align-items: flex-start; gap: 14px;
    color: var(--text-grey); font-size: 19px; font-weight: 400;
    letter-spacing: 1px; line-height: 1.35; margin-bottom: 14px;
  }
  .contact__icon { width: 16px; height: 16px; flex: none; margin-top: 4px; }
</style>
</head>
<body>
<main class="sheet">

  <section class="card card--front" aria-label="Card front">
    <div class="front__tab"></div>
    <div class="front__person">
      <h1 class="front__name">Dana Whitfield, Ph.D.</h1>
      <p class="front__title">Licensed Clinical Psychologist</p>
    </div>
    <div class="brand front__brand">
      <span class="brand__dot"></span>
      <p class="brand__name">Company Name</p>
    </div>
  </section>

  <section class="card card--back" aria-label="Card back">
    <svg class="back__band" viewBox="0 0 120 400" preserveAspectRatio="none" aria-hidden="true">
      <path d="M0 0 H70 C30 120 25 280 60 400 H0 Z" fill="var(--teal)"/>
      <path d="M70 0 C30 120 25 280 60 400 H48 C14 280 18 120 56 0 Z" fill="var(--teal-deep)" opacity=".5"/>
    </svg>
    <div class="back__decor"></div>
    <div class="brand back__brand">
      <span class="brand__dot"></span>
      <p class="brand__name">Company Name</p>
    </div>
    <div class="back__divider"></div>
    <ul class="contact">
      <li class="contact__item">
        <svg class="contact__icon" viewBox="0 0 16 16" aria-hidden="true"><circle cx="8" cy="8" r="7" fill="none" stroke="var(--teal)" stroke-width="1.5"/><path d="M5.5 4.5 L7 6 L6 7 Q7 9 9 10 L10 9 L11.5 10.5 L10.5 11.5 Q6 11 4.5 5.5 Z" fill="var(--teal)"/></svg>
        <span>312-555-0148</span>
      </li>
      <li class="contact__item">
        <svg class="contact__icon" viewBox="0 0 16 16" aria-hidden="true"><rect x="1.5" y="3.5" width="13" height="9" fill="none" stroke="var(--teal)" stroke-width="1.3"/><path d="M1.5 3.5 L8 9 L14.5 3.5" fill="none" stroke="var(--teal)" stroke-width="1.3"/></svg>
        <span>drdanawhitfield@mailbox.com</span>
      </li>
      <li class="contact__item">
        <svg class="contact__icon" viewBox="0 0 16 16" aria-hidden="true"><path d="M8 1 C4.5 1 3 3.5 3 6 C3 9.5 8 15 8 15 C8 15 13 9.5 13 6 C13 3.5 11.5 1 8 1 Z" fill="var(--teal)"/><circle cx="8" cy="6" r="2" fill="#fff"/></svg>
        <span>240 W. Harlow Suite 810<br>Chicago, Illinois 60610</span>
      </li>
    </ul>
  </section>

</main>
</body>
</html>
```